One of Australia's fastest growing Financial Company looking for an updated business card design!

Meridale Partners Australia is looking for an updated design for our business cards. We would like to keep up our professional appearances and have get new exciting design that fits our company.

The Meridale aim is to facilitate and assist clients in every financial requirement that may arise in financial areas.

We would to see the design to use colour blue and we like the clouds in the background. We have attached two designs we have use before but we need something with more professional and easy to read design.

We would like the website in the back of the card; the employees name more central and stands out; only a postal address; a list of all our locations along the bottom (Sydney, Melbourne, Brisbane, Singapore)

Looking forward to seeing the designs come in!

Target Market(s)

Other Industry Professionals
Middle Class Families

Industry/Entity Type

Finance

Contact Information for Business Card

Name; Company Role; Office Number; Mobile Number; Email Address; Website; Postal Address; Locations

Font styles to use
Serif
Sans Serif

Colors
0492cd
33a6d7
85cae6
85acd3
3176b5
0455a3
cee9f5
d5e2ee

Requirements
Must have
• Name; Company Role; Office Number; Mobile Number; Email Address; Website; Postal Address; Locations
Nice to have
• The colour blue, clouds on the background

```html
<!DOCTYPE html>
<html lang="en">
<head>
<meta charset="utf-8">
<title>Meridale Partners Australia – Business Card</title>
<link rel="stylesheet" href="https://fonts.googleapis.com/css2?family=Source+Sans+3:wght@400;600;700&display=swap">
<style>
  :root {
    --stage: #000000;
    --card-top: #2aa4de;
    --card-bottom: #1f80c7;
    --sky-deep: #0455a3;
    --sky-mid: #3176b5;
    --sky-light: #85cae6;
    --cloud: #e8f3fa;
    --ink: #ffffff;
  }
  * { margin: 0; padding: 0; box-sizing: border-box; }
  html, body {
    width: 1200px; height: 900px; overflow: hidden;
    background: var(--stage);
    font-family: "Source Sans 3", "Myriad Pro", Arial, sans-serif;
    color: var(--ink);
  }
  .card {
    position: absolute; top: 271px;
    width: 457px; height: 281px;
    border-radius: 13px; overflow: hidden;
  }
  /* Front */
  .card-front {
    left: 137px;
    background: linear-gradient(180deg, var(--card-top), var(--card-bottom));
    text-align: center;
  }
  .person {
    position: absolute; top: 23px; left: 0; right: 0;
    display: flex; justify-content: center; align-items: center; gap: 9px;
  }
  .person-name { font-size: 17px; font-weight: 700; letter-spacing: .2px; }
  .person-divider { width: 1px; height: 19px; background: var(--ink); }
  .person-role { font-size: 13px; font-weight: 400; }
  .brand {
    position: absolute; top: 60px; left: 0; right: 0;
    display: flex; justify-content: center; align-items: center; gap: 10px;
  }
  .brand-dot { width: 22px; height: 22px; border-radius: 50%; background: var(--ink); }
  .brand-name { font-size: 56px; font-weight: 400; line-height: 1; letter-spacing: -.5px; }
  .contacts {
    position: absolute; top: 129px; left: 0; right: 0;
    list-style: none; font-size: 13px; line-height: 19px;
  }
  .contacts li { display: flex; justify-content: center; align-items: center; gap: 4px; }
  .contacts svg { width: 9px; height: 9px; fill: var(--ink); }
  .address { position: absolute; top: 214px; left: 0; right: 0; font-size: 13px; }
  .locations {
    position: absolute; top: 241px; left: 0; right: 0;
    display: flex; justify-content: center; align-items: center; gap: 6px;
    font-size: 14.5px; font-weight: 700; list-style: none;
  }
  .locations li + li::before {
    content: ""; display: inline-block; width: 7px; height: 7px; border-radius: 50%;
    background: var(--ink); margin-right: 6px; vertical-align: 2px;
  }
  /* Back */
  .card-back { left: 626px; }
  .sky {
    position: absolute; inset: 0;
    background:
      radial-gradient(ellipse 60% 45% at 85% 25%, var(--cloud), transparent 70%),
      radial-gradient(ellipse 70% 30% at 60% 95%, var(--cloud), transparent 70%),
      linear-gradient(160deg, var(--sky-deep) 0%, var(--sky-mid) 45%, var(--sky-light) 100%);
  }
  .back-brand {
    position: absolute; left: 34px; top: 38px;
    font-size: 60px; font-weight: 400; line-height: 1; letter-spacing: -.5px;
  }
  .back-web { position: absolute; left: 48px; top: 106px; font-size: 16px; font-weight: 700; }
</style>
</head>
<body>
  <section class="card card-front">
    <div class="person">
      <span class="person-name">Daniel Hartley</span>
      <span class="person-divider"></span>
      <span class="person-role">Managing Director</span>
    </div>
    <div class="brand">
      <span class="brand-dot"></span>
      <span class="brand-name">Meridale</span>
    </div>
    <ul class="contacts">
      <li><svg viewBox="0 0 10 10"><path d="M2 0.5l2 2-1 1.2c.6 1.3 1.6 2.3 2.8 2.8l1.2-1 2 2-1.3 1.8C4.5 9.2.8 5.5.3 1.8z"/></svg>(044)-456-7890</li>
      <li><svg viewBox="0 0 10 10"><path d="M2.5 0h5v10h-5zM3.4 1v7h3.2V1z"/></svg>(044)-456-7890</li>
      <li><svg viewBox="0 0 10 10"><path d="M0 2h10v6H0zM.8 2.6 5 5.6l4.2-3"/></svg>info@youremail.com</li>
      <li><svg viewBox="0 0 10 10"><circle cx="5" cy="5" r="5"/></svg>www.website.com</li>
    </ul>
    <p class="address">12345, Address Goes Here&nbsp; Country Name, 123456</p>
    <ul class="locations">
      <li>Sydney</li><li>Melbourne</li><li>Brisbane</li><li>Singapore</li>
    </ul>
  </section>

  <section class="card card-back">
    <div class="sky" role="img" aria-label="Bright blue sky with white clouds and sun rays"></div>
    <span class="back-brand">Meridale</span>
    <span class="back-web">www.website.com</span>
  </section>
</body>
</html>
```